ベースの色はグリーンですが、その系統の配色か、必要に応じては青をいれてもらってもかまいません。コーポレートサイトのデザインですが、色々な方のパターンを見てみたいです。
採用も目的としているため比較的爽やかなイメージが良いかもしれません。
仕様書【ミライワークス用】.pdfと添付画像をもとにデザイン作成お願いします。

当選前提となった方は正式な社名及び連絡先をお伝えしますので修正対応をお願いします。
また希望の際は、当選後、中ページの制作及びコーディングも別途ご依頼可能です。
ページ数
1ページ
希望イメージ
シンプル 複雑
単色 カラフル
暗い 明るい
日常 高級
遊び心 厳粛
未来的 伝統的
女性的 男性的
希望する色
緑系、青系
納品ファイル
• 高解像度JPG (.jpg)
• フォトショップ形式 (.psd)
弊社で納品している運送系サイトを参考までに記載します。

https://www.harunomiya.co.jp/
https://www.mido-hakobi.co.jp/
https://www.tachibe-web.co.jp/
https://www.renkaru.net/
■ 選んだ理由

採用を意識したイメージと、全体のメリハリ感が非常にマッチしておりました。
ありがとうございます。

■ 提案者全員のお礼・コメント

たくさんのご提案ありがとうございます。
どれも非常にレベルが高く弊社デザイナー感でも意見が割れて迷いました。
またの機会がありましたらよろしくお願いいたします。

```html
<!DOCTYPE html>
<html lang="ja">
<head>
<meta charset="utf-8">
<title>株式会社〇〇運送</title>
<link href="https://fonts.googleapis.com/css2?family=Noto+Sans+JP:wght@400;500;700;900&family=Roboto:wght@400;700&display=swap" rel="stylesheet">
<style>
:root{
  --green:#1f9e78;
  --green-dark:#12805f;
  --green-deep:#0e6e52;
  --green-pale:#e3f1ec;
  --mint:#2bb08a;
  --ink:#2d3a36;
  --muted:#6c7a75;
  --white:#ffffff;
  --gray:#eef1f0;
}
*{margin:0;padding:0;box-sizing:border-box}
html,body{width:1200px;height:3060px;overflow:hidden}
body{font-family:"Noto Sans JP",sans-serif;color:var(--ink);background:var(--white);position:relative}
.en{font-family:"Roboto",sans-serif}
.abs{position:absolute}

/* header */
.site-header{position:absolute;top:0;left:0;width:1200px;height:60px;background:var(--white);display:flex;align-items:center;padding:0 24px;z-index:5}
.logo{font-size:17px;font-weight:700;color:var(--ink);display:flex;align-items:center;gap:8px}
.logo-mark{width:14px;height:14px;background:var(--green)}
.global-nav{margin-left:auto;display:flex;gap:22px;font-size:12px;color:var(--ink)}
.header-btn{margin-left:26px;background:var(--green);color:#fff;font-size:12px;padding:10px 16px}
.header-tel{margin-left:16px;color:var(--green-dark);line-height:1.1}
.header-tel b{font-family:"Roboto",sans-serif;font-size:18px;display:block}
.header-tel small{font-size:9px;color:var(--muted)}

/* hero */
.hero{top:0;left:0;width:1200px;height:680px;overflow:hidden}
.hero-photo{position:absolute;inset:0;background:linear-gradient(120deg,#a9c8d6 0%,#dfe9ee 40%,#c7d3d6 70%,#8da4a5 100%)}
.hero-panel{position:absolute;inset:0}
.hero-copy{position:absolute;left:64px;top:270px;color:#fff}
.hero-copy .lead{font-size:22px;font-weight:700;letter-spacing:.04em}
.hero-copy .catch{font-family:"Roboto",sans-serif;font-size:40px;font-weight:700;margin-top:6px}
.hero-copy p{font-size:15px;line-height:2;margin-top:30px}

/* band */
.band{top:680px;left:0;width:1200px;height:240px;background:linear-gradient(90deg,#5fa64a,#a9d46c 45%,#e8f3c8 55%,#7cba54)}
.notice{position:absolute;left:472px;top:740px;width:416px;height:120px;background:#fff;display:flex;align-items:center;gap:18px;padding:0 22px}
.notice-badge{width:90px;height:70px;background:var(--green-pale);border:2px solid var(--green)}
.notice p{font-size:11px;line-height:1.8;color:var(--ink);flex:1}

/* headings */
.sec-title{text-align:center;position:absolute;left:0;width:1200px}
.sec-title h2{font-size:26px;font-weight:700}
.sec-title span{font-family:"Roboto",sans-serif;font-size:11px;color:var(--green);letter-spacing:.15em}

/* service */
.service-bg{top:1380px;left:0;width:1200px;height:370px}
.service-photo{top:1048px;left:0;width:1200px;height:352px;background:linear-gradient(100deg,#c9d7e2 0%,#3f5fa8 30%,#e6eaee 55%,#b9c7cc 80%,#7f9799 100%)}
.service-box{top:1372px;left:464px;width:728px;height:260px;background:#fff;padding:34px 40px;box-shadow:0 4px 18px rgba(0,0,0,.08)}
.service-box p{font-size:12px;line-height:2;color:var(--muted)}
.btn{display:inline-block;background:var(--green);color:#fff;font-size:12px;padding:8px 26px}
.service-box .btn{position:absolute;right:140px;bottom:42px}

/* tiles */
.tile{position:absolute;display:flex;flex-direction:column;align-items:center;justify-content:center;color:#fff}
.tile h3{font-size:22px;font-weight:700;text-shadow:0 1px 6px rgba(0,0,0,.3)}
.tile span{font-family:"Roboto",sans-serif;font-size:10px;letter-spacing:.12em}
.tile-env{top:1748px;left:0;width:600px;height:188px;background:linear-gradient(135deg,#3e7c3a,#8dbb5a 60%,#4e8f45)}
.tile-biz{top:1748px;left:600px;width:600px;height:188px;background:linear-gradient(135deg,#6a7078,#b5463e 55%,#8c8f94)}
.tile-company{top:1936px;left:0;width:1200px;height:184px;background:linear-gradient(180deg,#a9bfd4,#d9e1e8 60%,#c3cdd4)}

/* recruit */
.recruit-bg{top:2120px;left:0;width:1200px;height:440px;background:var(--gray)}
.recruit-photo{top:2180px;left:600px;width:600px;height:320px;background:linear-gradient(120deg,#e9eef2,#9fb3c4 45%,#2f5ea8 70%,#d9dee2)}
.recruit-card{top:2180px;left:232px;width:368px;height:320px;background:#fff;padding:46px 40px}
.recruit-card h2{font-size:26px;font-weight:700}
.recruit-card .en{font-size:11px;color:var(--green);letter-spacing:.15em}
.recruit-card p{font-size:11px;line-height:1.9;color:var(--muted);margin:26px 0 22px}

/* contact & footer */
.green-base{top:2760px;left:0;width:1200px;height:300px;background:var(--green)}
.contact-card{top:2560px;left:232px;width:736px;height:380px;background:#fff;text-align:center;padding-top:30px}
.contact-card h2{font-size:26px;font-weight:700}
.contact-card .en{font-size:11px;color:var(--green);letter-spacing:.15em}
.contact-card p{font-size:11px;line-height:1.9;color:var(--muted);margin-top:22px}
.contact-row{display:flex;margin:44px 88px 0}
.contact-tel{flex:1;height:80px;background:var(--green-deep);color:#fff;display:flex;flex-direction:column;justify-content:center;align-items:center}
.contact-tel b{font-family:"Roboto",sans-serif;font-size:26px;display:flex;align-items:center;gap:8px}
.contact-tel small{font-size:10px}
.contact-mail{flex:1;height:80px;background:var(--mint);color:#fff;display:flex;align-items:center;justify-content:center;gap:10px;font-size:16px;font-weight:500}

.site-footer{top:2960px;left:0;width:1200px;height:100px;color:#fff;padding:0 232px}
.footer-logo{font-size:18px;font-weight:700}
.site-footer address{font-style:normal;font-size:10px;line-height:1.7;margin-top:6px;opacity:.9}
.footer-nav{position:absolute;left:740px;top:0;display:grid;grid-template-columns:repeat(2,120px);gap:6px 20px;font-size:11px}
</style>
</head>
<body>

<header class="site-header">
  <div class="logo"><span class="logo-mark"></span>株式会社〇〇運送</div>
  <nav class="global-nav"><span>会社案内</span><span>事業案内</span><span>環境保護方針</span><span>採用情報</span><span>お知らせ</span></nav>
  <div class="header-btn">お問い合わせ</div>
  <div class="header-tel"><b>1,000-000-0000</b><small>受付時間 9:00〜18:00（土日祝除く）</small></div>
</header>

<section class="hero abs">
  <div class="hero-photo" role="img" aria-label="整列した大型トラックの写真"></div>
  <svg class="hero-panel" width="1200" height="680" viewBox="0 0 1200 680">
    <polygon points="0,60 500,60 340,680 0,680" fill="#1f9e78" opacity=".95"/>
    <polygon points="500,60 580,60 420,680 340,680" fill="#2bb08a" opacity=".55"/>
  </svg>
  <div class="hero-copy">
    <div class="lead">安全・安心・信頼される企業として</div>
    <div class="catch">Reliability &amp; safety &amp; reliability</div>
    <p>長年の経験と実績を活かし、<br>お客様の様々なニーズにお応えできるよう、<br>質の高いサービスを提供してまいります。</p>
  </div>
</section>

<div class="band abs" role="img" aria-label="木漏れ日の差す新緑の写真"></div>
<div class="notice">
  <div class="notice-badge" role="img" aria-label="認定マーク"></div>
  <p>弊社は、国土交通省が推進する安全性優良事業所の認定を受けています。安全で確実な輸送を約束し、お客様に安心してご利用いただける体制を整えております。</p>
</div>

<div class="sec-title" style="top:960px"><h2>事業内容</h2><span>SERVICE</span></div>

<svg class="service-bg abs" width="1200" height="370" viewBox="0 0 1200 370">
  <polygon points="0,0 1200,0 1200,370 0,260" fill="#e3f1ec"/>
</svg>
<div class="service-photo abs" role="img" aria-label="並んで停車するトラックの写真"></div>
<div class="service-box abs">
  <p>私たちは地域に根ざした運送会社として、一般貨物から大型輸送まで幅広く対応しております。経験豊富なドライバーと整備された車両で、お客様の大切なお荷物を安全かつ迅速にお届けします。物流のことならどんなことでもお気軽にご相談ください。</p>
  <span class="btn">詳細はこちら</span>
</div>

<div class="tile tile-env" role="img" aria-label="若葉と自然の写真"><h3>環境保護方針</h3><span>ENVIRONMENTAL POLICY</span></div>
<div class="tile tile-biz" role="img" aria-label="赤いトラックの写真"><h3>事業案内</h3><span>BUSINESS</span></div>
<div class="tile tile-company" role="img" aria-label="社屋の外観写真"><h3>会社案内</h3><span>COMPANY</span></div>

<div class="recruit-bg abs"></div>
<div class="recruit-photo abs" role="img" aria-label="トラックの前に立つ作業服姿の社員の写真"></div>
<div class="recruit-card abs">
  <h2>採用情報</h2>
  <div class="en">RECRUIT</div>
  <p>一緒に働く仲間を募集しています。<br>未経験の方も安心してスタートできます。</p>
  <span class="btn">詳細はこちら</span>
</div>

<div class="green-base abs"></div>
<div class="contact-card abs">
  <h2>お問い合わせ</h2>
  <div class="en">CONTACT</div>
  <p>運送のご依頼やお見積り、採用に関するご質問はお気軽にどうぞ。<br>お電話またはメールフォームよりご連絡ください。</p>
  <div class="contact-row">
    <div class="contact-tel">
      <b><svg width="20" height="20" viewBox="0 0 24 24"><path d="M6.6 10.8a15 15 0 006.6 6.6l2.2-2.2a1 1 0 011-.25 11.4 11.4 0 003.6.57 1 1 0 011 1V20a1 1 0 01-1 1A17 17 0 013 4a1 1 0 011-1h3.5a1 1 0 011 1 11.4 11.4 0 00.57 3.6 1 1 0 01-.25 1z" fill="#fff"/></svg>000-000-0000</b>
      <small>受付時間 9:00〜18:00（土日祝除く）</small>
    </div>
    <div class="contact-mail">
      <svg width="22" height="16" viewBox="0 0 22 16"><rect x="1" y="1" width="20" height="14" fill="none" stroke="#fff" stroke-width="1.6"/><path d="M1 1l10 8 10-8" fill="none" stroke="#fff" stroke-width="1.6"/></svg>お問い合わせ
    </div>
  </div>
</div>

<footer class="site-footer abs">
  <div class="footer-logo">株式会社〇〇運送</div>
  <address>〒000-0000 〇〇県〇〇市〇〇町0-0-0<br>TEL 000-000-0000</address>
  <nav class="footer-nav"><span>ホーム</span><span>採用情報</span><span>会社案内</span><span>お知らせ</span><span>事業案内</span><span>お問い合わせ</span><span>環境保護方針</span></nav>
</footer>

</body>
</html>
```